engineering and fabrication company- KelbroTek

We require a full functional and coded website design for an engineering and fabrication company in Western Australia.
I have attached capability statement with a content of this website.
I would like to have Fabrication services divided into two sections

1. Steel Fabrication
2. Plastic Fabrication

Industry/Entity Type

mining , waste water , oil and gas , engineering and design

Coding

Coded - Design and coding required

Number of Pages Required

5+ page

Colors
0054AA
0677BA
7BADD7
CADEEF
E8F1F8
0094D4
00A9DD
6FCCEA
C7EBF8
E9F6FB

Requirements
Must have
• Must look very professional

```html
<!DOCTYPE html>
<html lang="en">
<head>
<meta charset="utf-8">
<title>KelbroTek – Design, Engineering and Fabrication</title>
<link href="https://fonts.googleapis.com/css2?family=Poppins:wght@400;500;600;700&family=Titillium+Web:wght@600;700&display=swap" rel="stylesheet">
<style>
:root{
  --blue:#0054AA;
  --blue-mid:#0677BA;
  --sky:#0094D4;
  --sky-2:#00A9DD;
  --ice:#E8F1F8;
  --ice-2:#F0F6FA;
  --navy:#0A1835;
  --navy-2:#0D2148;
  --ink:#1B1B1B;
  --text:#555;
  --white:#fff;
  --star:#8CC63F;
}
*{box-sizing:border-box;margin:0;padding:0}
html,body{width:1200px;height:4326px;overflow:hidden}
body{position:relative;font-family:"Poppins",sans-serif;color:var(--text);background:var(--white)}
.abs{position:absolute}
.head{font-family:"Titillium Web",sans-serif;font-weight:700;text-transform:uppercase;line-height:1.1}
.head .accent{color:var(--sky)}
.sub{font-size:12px;color:#555;text-align:center}

.btn{position:absolute;display:flex;align-items:center;justify-content:center;height:34px;width:112px;background:var(--blue);color:var(--white);font-size:12px;clip-path:polygon(0 0,100% 0,90% 100%,0 100%)}
.btn::after{content:"";position:absolute;right:6px;top:0;width:6px;height:100%;background:var(--sky);transform:skewX(-18deg)}

/* top bar + nav */
.topbar{left:0;top:0;width:1200px;height:37px;background:var(--navy);color:var(--white);font-size:12px;display:flex;align-items:center;justify-content:center}
.logo-box{left:56px;top:0;width:140px;height:102px;background:var(--white);border-top:4px solid var(--blue)}
.logo-name{font-weight:700;font-size:20px;color:var(--blue);letter-spacing:.5px;text-align:center;margin-top:30px}
.logo-tag{font-size:7px;color:#777;text-align:center;margin-top:4px}
.nav{left:324px;top:58px;display:flex;gap:34px;font-size:12px;font-weight:500;color:var(--ink)}
.nav .on{border-bottom:2px solid var(--sky);padding-bottom:8px}
.search{left:856px;top:58px}
.mail-box{left:948px;top:37px;width:252px;height:67px;background:var(--blue-mid);clip-path:polygon(22px 0,100% 0,100% 100%,0 100%);color:var(--white)}
.mail-box svg{position:absolute;left:38px;top:18px}
.mail-box .l1{position:absolute;left:92px;top:12px;font-size:11px}
.mail-box .l2{position:absolute;left:92px;top:33px;font-size:13px;font-weight:600}

/* hero */
.hero{left:0;top:104px;width:1200px;height:584px;background:linear-gradient(120deg,#3a2a1c 0%,#6a4a22 25%,#1c2c55 55%,#0c1d44 100%);clip-path:polygon(0 0,100% 0,100% 524px,700px 584px,0 524px)}
.hero-shade{left:0;top:104px;width:1200px;height:584px;background:rgba(8,22,52,.45);clip-path:polygon(0 0,100% 0,100% 524px,700px 584px,0 524px)}
.hero-title{left:0;top:232px;width:1200px;text-align:center;color:var(--white);font-family:"Titillium Web",sans-serif;font-weight:600;font-size:48px;line-height:56px}
.hero-text{left:220px;top:352px;width:760px;text-align:center;color:var(--white);font-size:12.5px;line-height:22px}

/* commitments */
.commit-title{left:0;top:752px;width:1200px;text-align:center;font-size:34px;color:var(--navy)}
.commit-sub{left:0;top:798px;width:1200px}
.commit{top:834px;width:320px;text-align:center}
.commit svg{display:block;margin:0 auto}
.commit h3{font-size:14px;font-weight:500;color:var(--ink);margin-top:22px}
.commit p{font-size:12px;line-height:22px;margin-top:10px}

/* innovative */
.innov{left:0;top:1150px;width:1200px;height:532px;background:var(--ice)}
.innov-photo{left:512px;top:1150px;width:688px;height:532px;background:linear-gradient(135deg,#b9c4cf,#6f7f93 55%,#2c3a52);clip-path:polygon(277px 0,100% 0,100% 100%,0 100%)}
.innov-stripe{left:512px;top:1262px;width:230px;height:420px;background:var(--blue-mid);clip-path:polygon(210px 0,230px 0,22px 100%,0 100%)}
.innov-h1{left:62px;top:1236px;font-size:32px;color:var(--sky)}
.innov-h2{left:62px;top:1282px;font-size:32px;color:var(--ink)}
.innov-text{left:62px;top:1330px;width:500px;font-size:12px;line-height:22px}
.innov-text p+p{margin-top:10px}

/* services */
.serv-title{left:0;top:1765px;width:1200px;text-align:center;font-size:34px;color:var(--ink)}
.serv-sub{left:0;top:1811px;width:1200px}
.steel-accent{left:0;top:1848px;width:60px;height:40px;background:var(--blue);clip-path:polygon(0 0,100% 0,0 100%)}
.steel-photo{left:0;top:1872px;width:596px;height:450px;background:linear-gradient(160deg,#5c6670,#2d343b 50%,#8a5a3a);clip-path:polygon(0 0,100% 0,496px 100%,0 100%)}
.plastic-accent{left:1140px;top:2380px;width:60px;height:40px;background:var(--blue);clip-path:polygon(0 0,100% 0,100% 100%)}
.plastic-photo{left:604px;top:2404px;width:596px;height:451px;background:linear-gradient(200deg,#9aa6b4,#3b4656 45%,#15182a);clip-path:polygon(0 0,100% 0,100% 100%,101px 100%)}
.serv-title-sm{font-size:32px;color:var(--sky)}
.serv-text{width:475px;font-size:12px;line-height:22px}

/* clients */
.clients{left:0;top:2970px;width:1200px;height:453px;background:var(--ice-2)}
.clients-title{left:0;top:3016px;width:1200px;text-align:center;font-size:32px;color:var(--ink)}
.card{top:3110px;width:517px;height:251px;background:var(--white);text-align:center;padding:0 62px}
.card .stars{margin-top:40px;color:var(--star);font-size:13px;letter-spacing:2px}
.card h4{font-size:13px;font-weight:500;color:var(--blue-mid);margin-top:2px}
.card p{font-size:12px;line-height:21px;margin-top:10px}
.quote{top:3090px;width:40px;height:40px;background:var(--ice-2);display:flex;align-items:center;justify-content:center}

/* contact */
.contact-photo{left:0;top:3427px;width:700px;height:600px;background:linear-gradient(140deg,#4b5a66,#1f2b38 45%,#6b5a45);}
.contact-blue{left:520px;top:3427px;width:680px;height:600px;background:var(--blue-mid);clip-path:polygon(143px 0,100% 0,100% 500px,0 584px)}
.contact-title{left:660px;top:3496px;width:478px;text-align:center;font-size:32px;color:var(--white)}
.field{background:var(--white);border:1px solid #d6e2ee;font-size:11px;color:#666;padding:10px 12px}
.footer{left:0;top:4000px;width:1200px;height:326px;background:var(--navy);clip-path:polygon(0 27px,1200px 0,100% 100%,0 100%)}
.foot-name{left:60px;top:4058px;width:230px;text-align:center;font-weight:700;font-size:26px;color:var(--sky)}
.foot-tag{left:60px;top:4205px;width:230px;text-align:center;font-size:11px;color:#9fb3cc}
.foot-col{top:4060px}
.foot-col h5{font-size:13px;font-weight:500;color:var(--sky);margin-bottom:12px}
.foot-col li{list-style:none;font-size:11px;color:var(--white);line-height:29px}
.contact-line{display:flex;gap:14px;align-items:flex-start;font-size:11px;color:var(--white);line-height:18px;margin-bottom:12px}
.copy{left:0;top:4292px;width:1200px;text-align:center;font-size:11px;color:var(--white)}
.copy span{color:var(--sky)}
</style>
</head>
<body>

<!-- header -->
<div class="abs topbar">Lorem Ipsum is simply dummy text of the printing and typesetting industry.</div>
<div class="abs logo-box">
  <div class="logo-name">KELBROTEK</div>
  <div class="logo-tag">Design · Engineering · Fabrication</div>
</div>
<nav class="abs nav">
  <span class="on">HOME</span><span>ABOUT US</span><span>FABRICATION SERVICES</span><span>BLOG</span><span>CONTACT US</span>
</nav>
<svg class="abs search" width="18" height="18" viewBox="0 0 18 18" fill="none" stroke="#1b1b1b" stroke-width="2"><circle cx="7.5" cy="7.5" r="5.5"/><path d="M12 12l5 5"/></svg>
<div class="abs mail-box">
  <svg width="34" height="30" viewBox="0 0 34 30" fill="none" stroke="#fff" stroke-width="1.6"><path d="M2 12l15-10 15 10v16H2z"/><path d="M2 12l15 10 15-10"/><circle cx="17" cy="11" r="4"/></svg>
  <div class="l1">E-mail us</div>
  <div class="l2">info@kelbrotek.com.au</div>
</div>

<!-- hero -->
<div class="abs hero" role="img" aria-label="Welder in a helmet working with sparks flying"></div>
<div class="abs hero-shade"></div>
<h1 class="abs hero-title">KelbroTek, is a multi-disciplinary<br>design/engineering and fabrication.</h1>
<p class="abs hero-text">The guiding force in all that we do is our commitment to providing hands-on reliable customer service and quality metal and plastic components for a broad range of industries including Mining, Chemical Industry, Oil and Gas , Water Treatment, Agricultural Equipment, Material Handling, Construction Equipment, Renewable Energy &amp; more.</p>
<div class="btn" style="left:542px;top:458px">Learn More</div>

<!-- commitments -->
<h2 class="abs head commit-title"><span class="accent">Our Commitments</span> to you</h2>
<p class="abs sub commit-sub">With every job we take on, KelbroTek promises to deliver</p>

<div class="abs commit" style="left:88px">
  <svg width="112" height="110" viewBox="0 0 112 110" fill="none" stroke="#0677BA" stroke-width="1.5"><path d="M56 4L108 106H4z"/><path d="M56 14L98 100H14z" stroke="#7BADD7" stroke-dasharray="3 3"/><circle cx="56" cy="64" r="14"/><path d="M56 56l3 6 6 1-4.5 4 1 6-5.5-3-5.5 3 1-6-4.5-4 6-1z"/><path d="M48 76l-4 14 6-3 4 5 2-12M64 76l4 14-6-3-4 5"/></svg>
  <h3>QUALITY</h3>
  <p>We understand the level of precision required to seamlessly carry out fabrication projects, so our processes are designed to guarantee the highest level of quality on every job.</p>
</div>
<div class="abs commit" style="left:440px">
  <svg width="112" height="110" viewBox="0 0 112 110" fill="none" stroke="#0677BA" stroke-width="1.5"><path d="M56 4L108 106H4z"/><path d="M56 14L98 100H14z" stroke="#7BADD7" stroke-dasharray="3 3"/><rect x="44" y="52" width="22" height="30"/><path d="M48 60h14M48 66h14M48 72h8"/><circle cx="66" cy="78" r="6"/><path d="M70 82l6 6"/></svg>
  <h3>TRANSPARENCY</h3>
  <p>From initial budget estimates to the end of construction, our team is dedicated to transparency throughout the entire process, so you always know where your project stands.</p>
</div>
<div class="abs commit" style="left:794px">
  <svg width="112" height="110" viewBox="0 0 112 110" fill="none" stroke="#0677BA" stroke-width="1.5"><path d="M56 4L108 106H4z"/><path d="M56 14L98 100H14z" stroke="#7BADD7" stroke-dasharray="3 3"/><circle cx="56" cy="64" r="9"/><path d="M44 64a12 12 0 0 1 24 0"/><path d="M40 92c2-10 8-14 16-14s14 4 16 14"/></svg>
  <h3>SUPPORT</h3>
  <p>A dedicated project team, including some of our top executives, will guide you through your project. When you have questions or concerns, we're right by your side.</p>
</div>

<!-- innovative -->
<div class="abs innov"></div>
<div class="abs innov-photo" role="img" aria-label="Engineer and manager reviewing plans in a fabrication workshop beside a steel tank"></div>
<div class="abs innov-stripe"></div>
<h2 class="abs head innov-h1">Innovative Fabrication Services</h2>
<h2 class="abs head innov-h2">From a team you trust</h2>
<div class="abs innov-text">
  <p>KelbroTek operates steel and plastic fabrication facilities, utilizing the latest high-tech machinery and cutting-edge computer-driven processes to bring the pieces you need to life with the precision you rely on.</p>
  <p>Our team of enthusiastic and highly skilled and qualified tradesmen put their craftmanship, knowledge, and passion into every piece that leaves our plants . We can fabricate almost any item from a huge range of mild steel, and stainless steel as well as variety of plastic materials. All fabrication is performed and inspected under strict quality assurance program.</p>
</div>
<div class="btn" style="left:60px;top:1549px">Learn More</div>

<!-- fabrication services -->
<h2 class="abs head serv-title"><span class="accent">Fabrication</span> Services</h2>
<p class="abs sub serv-sub">With every job we take on, KelbroTek promises to deliver</p>

<div class="abs steel-accent"></div>
<div class="abs steel-photo" role="img" aria-label="Row of steel pipes fitted with orange valve wheels"></div>
<svg class="abs" style="left:666px;top:1941px" width="90" height="90" viewBox="0 0 90 90" fill="none" stroke="#0054AA" stroke-width="2"><rect x="4" y="6" width="14" height="80"/><path d="M18 14h22v14H18M40 20h6"/><rect x="52" y="4" width="24" height="44" rx="2"/><rect x="57" y="10" width="14" height="12"/><path d="M64 48v10M46 86h40M54 86V66h20v20"/><circle cx="46" cy="66" r="7"/></svg>
<h3 class="abs head serv-title-sm" style="left:666px;top:2043px">Steel Fabrication</h3>
<p class="abs serv-text" style="left:666px;top:2090px">Lorem Ipsum is simply dummy text of the printing and typesetting industry. Lorem Ipsum has been the industry's standard dummy text ever since the 1500s, when an unknown printer took a galley of type and scrambled it to make a type specimen book. It has survived not only five centuries, but also the leap into electronic typesetting, remaining essentially unchanged.</p>
<div class="btn" style="left:666px;top:2240px">Learn More</div>

<div class="abs plastic-accent"></div>
<div class="abs plastic-photo" role="img" aria-label="Stacked black plastic pipes with blue stripes in a factory"></div>
<svg class="abs" style="left:62px;top:2492px" width="92" height="84" viewBox="0 0 92 84" fill="none" stroke="#0054AA" stroke-width="2"><rect x="4" y="4" width="30" height="44"/><path d="M12 20v16h12"/><path d="M40 20l16-4 12 18-14 12z"/><path d="M2 64c6-6 12 6 18 0s12 6 18 0 12 6 18 0 12 6 18 0 12 6 18 0"/><path d="M2 76c6-6 12 6 18 0s12 6 18 0 12 6 18 0 12 6 18 0 12 6 18 0" stroke="#0094D4"/></svg>
<h3 class="abs head serv-title-sm" style="left:62px;top:2602px">Plastic Fabrication</h3>
<p class="abs serv-text" style="left:62px;top:2651px">Lorem Ipsum is simply dummy text of the printing and typesetting industry. Lorem Ipsum has been the industry's standard dummy text ever since the 1500s, when an unknown printer took a galley of type and scrambled it to make a type specimen book. It has survived not only five centuries, but also the leap into electronic typesetting, remaining essentially unchanged.</p>
<div class="btn" style="left:60px;top:2800px">Learn More</div>

<!-- clients -->
<div class="abs clients"></div>
<h2 class="abs head clients-title"><span class="accent">Our Happy</span> Clients</h2>
<svg class="abs" style="left:38px;top:3196px" width="40" height="16" viewBox="0 0 40 16" fill="none" stroke="#0677BA" stroke-width="1.8"><path d="M40 8H2M9 1L2 8l7 7"/></svg>
<svg class="abs" style="left:1122px;top:3196px" width="40" height="16" viewBox="0 0 40 16" fill="none" stroke="#333" stroke-width="1.8"><path d="M0 8h38M31 1l7 7-7 7"/></svg>

<div class="abs card" style="left:60px">
  <div class="stars">★★★★★</div>
  <h4>Customer Name</h4>
  <p>Lorem Ipsum is simply dummy text of the printing and typesetting industry. Lorem Ipsum has been the industry's standard dummy text ever since the 1500s, when an unknown printer took a galley of type and scrambled it to make a type specimen book. It has survived not only.</p>
</div>
<div class="abs quote" style="left:298px"><svg width="28" height="22" viewBox="0 0 28 22" fill="#0677BA"><path d="M0 0h12v12L6 22H1l4-10H0zM16 0h12v12l-6 10h-5l4-10h-5z"/></svg></div>
<div class="abs card" style="left:622px">
  <div class="stars">★★★★★</div>
  <h4>Customer Name</h4>
  <p>Lorem Ipsum is simply dummy text of the printing and typesetting industry. Lorem Ipsum has been the industry's standard dummy text ever since the 1500s, when an unknown printer took a galley of type and scrambled it to make a type specimen book. It has survived not only.</p>
</div>
<div class="abs quote" style="left:861px"><svg width="28" height="22" viewBox="0 0 28 22" fill="#0677BA"><path d="M0 0h12v12L6 22H1l4-10H0zM16 0h12v12l-6 10h-5l4-10h-5z"/></svg></div>

<!-- contact -->
<div class="abs contact-photo" role="img" aria-label="Factory worker in a hard hat standing with arms crossed"></div>
<div class="abs contact-blue"></div>
<h2 class="abs head contact-title">Get in touch</h2>
<div class="abs field" style="left:676px;top:3557px;width:225px;height:36px">Full Name*</div>
<div class="abs field" style="left:914px;top:3557px;width:225px;height:36px">E-mail*</div>
<div class="abs field" style="left:676px;top:3609px;width:225px;height:36px">Phone No.*</div>
<div class="abs field" style="left:914px;top:3609px;width:225px;height:36px">Subject*</div>
<div class="abs field" style="left:676px;top:3658px;width:463px;height:131px">Massege*</div>
<div class="btn" style="left:846px;top:3831px;width:98px">Submit</div>

<!-- footer -->
<div class="abs footer"></div>
<div class="abs foot-name">KELBROTEK</div>
<div class="abs foot-tag">Design / Engineering / Fabrication</div>

<div class="abs foot-col" style="left:337px">
  <h5>Site Map</h5>
  <ul><li>HOME</li><li>ABOUT US</li><li>FABRICATION SERVICES</li><li>BLOG</li><li>CONTACT US</li></ul>
</div>
<div class="abs foot-col" style="left:616px">
  <h5>Services</h5>
  <ul><li>PLASTIC FBRICATION</li><li>STEEL FBRICATION</li></ul>
</div>
<div class="abs foot-col" style="left:891px;width:260px">
  <h5>Contact Us Today</h5>
  <div class="contact-line"><svg width="14" height="18" viewBox="0 0 14 18" fill="none" stroke="#fff" stroke-width="1.4"><path d="M7 17s6-6 6-10A6 6 0 0 0 1 7c0 4 6 10 6 10z"/><circle cx="7" cy="7" r="2"/></svg><span>Unit 4 / 27 Forge Street Kewdale WA 6105</span></div>
  <div class="contact-line"><svg width="16" height="16" viewBox="0 0 16 16" fill="none" stroke="#fff" stroke-width="1.4"><path d="M3 1l3 3-2 2c1 3 3 5 6 6l2-2 3 3-2 2C7 15 1 9 1 3z"/></svg><span style="font-weight:600">123 456 7890</span></div>
  <div class="contact-line"><svg width="18" height="14" viewBox="0 0 18 14" fill="none" stroke="#fff" stroke-width="1.4"><rect x="1" y="1" width="16" height="12"/><path d="M1 1l8 7 8-7"/></svg><span>info@kelbrotek.com.au</span></div>
</div>

<p class="abs copy">© 2022 <span>Engineering Fabrication KelbroTek</span>. | All Rights Reserved.</p>

</body>
</html>
```